Need webdesign for service company that provides Car hiring service and transit service

We need a web design for a company that provides airport transit services and transport services including Limo, Corporate cars, Disability transit, Family transit service. We need is a simple and professional design.

Below is site which we like and also offer the same service http://www.ridelyntrek.com.au/

Reason: Waiting for the Feedback from multiple stakeholders. Need the time to select and approve the design

Target Market(s)

Tourism, Travel

Industry/Entity Type

Airport

Number of Pages Required

3 page

Font styles to use
Decorative
Script

Requirements
Must have
• Simple and Professional, Site we like http://www.ridelyntrek.com.au/ and also need to mobile friendly
Should not have
• Shouldn't have too many images

```html
<!DOCTYPE html>
<html lang="en">
<head>
<meta charset="utf-8">
<title>Rovella — Private &amp; Business Transport</title>
<link rel="stylesheet" href="https://fonts.googleapis.com/css2?family=Roboto:wght@300;400;700&display=swap">
<style>
  :root{
    --black:#000;
    --panel:#2b2b2b;
    --band:#24272b;
    --accent:#f5475a;
    --ink:#333;
    --muted:#555;
    --field:#e6e6e6;
    --white:#fff;
    --footer-ink:#777;
  }
  *{box-sizing:border-box;margin:0;padding:0}
  html,body{width:1200px;height:1038px;overflow:hidden;background:var(--white)}
  body{font-family:"Roboto",Arial,sans-serif;color:var(--ink);position:relative}

  .site-header{position:absolute;left:0;top:0;width:1200px;height:112px;background:var(--black)}
  .brand-name{position:absolute;left:158px;top:36px;color:var(--white);font-size:32px;line-height:36px;font-weight:300;letter-spacing:.5px}
  .header-tools{position:absolute;right:157px;top:42px;display:flex;gap:26px}
  .header-tools svg{width:28px;height:28px;fill:none;stroke:var(--white);stroke-width:3}

  .intro{position:absolute;left:0;top:160px;width:1200px;text-align:center}
  .intro h1{font-size:48px;font-weight:300;line-height:58px}
  .intro h1 strong{font-weight:700}
  .intro h2{font-size:28px;font-weight:300;line-height:30px}
  .intro p{width:870px;margin:18px auto 0;font-size:13.6px;line-height:18px;font-weight:300;color:var(--muted)}

  .quote{position:absolute;left:158px;top:365px;width:284px;height:351px;background:var(--panel);padding:18px 21px}
  .quote h3{font-size:21px;font-weight:400;letter-spacing:3px;color:var(--white);line-height:26px}
  .quote h3 .hl{color:var(--accent)}
  .quote h3 b{font-weight:700}
  .field{display:block;width:242px;height:30px;margin-top:11px;background:var(--field);font:300 12.5px "Roboto",sans-serif;color:#666;padding:0 10px;line-height:30px;white-space:nowrap;overflow:hidden}
  .field + .field{margin-top:18px}
  .option{display:flex;align-items:center;gap:8px;color:#ddd;font-size:12.5px;font-weight:300;margin-top:12px}
  .option:first-of-type{margin-top:24px}
  .option-icon{width:17px;height:17px;background:#ddd;border-radius:2px;display:flex;align-items:center;justify-content:center}
  .btn{display:flex;align-items:center;justify-content:center;background:var(--accent);color:var(--white);font-size:19px;font-weight:400;border-radius:2px}
  .btn b{font-weight:700;margin-left:5px}
  .quote .btn{width:242px;height:48px;margin-top:26px}
  .quote small{display:block;margin-top:12px;font-size:11px;color:#ddd}
  .quote small span{color:var(--accent)}

  .feature{position:absolute;left:458px;top:365px;width:584px}
  .feature-tiles{display:flex;height:216px}
  .tile{position:relative;width:292px;height:216px}
  .tile-photo{position:absolute;inset:0 0 54px 0}
  .tile-luxury .tile-photo{background:linear-gradient(120deg,#222 0%,#9a9a9a 45%,#1a1a1a 80%)}
  .tile-style .tile-photo{background:linear-gradient(160deg,#0c0f14 10%,#3d4652 50%,#10141a 85%)}
  .tile-label{position:absolute;left:0;bottom:0;width:100%;height:54px;background:#151719;color:var(--white);font-size:21px;font-weight:700;letter-spacing:2.5px;padding:15px 20px}
  .tile-style .tile-label{background:#1c2026}
  .feature p{margin-top:18px;font-size:13.6px;line-height:18px;font-weight:300;color:var(--muted)}
  .feature .btn{width:142px;height:48px;margin-top:20px}

  .benefits{position:absolute;left:0;top:786px;width:1200px;height:203px;background:var(--band);display:flex;justify-content:center;gap:13px;padding-top:56px}
  .benefit{width:212px;text-align:center;color:#ccc;font-size:12.5px;font-weight:300;line-height:18px}
  .benefit svg{width:30px;height:30px;fill:var(--white);margin-bottom:14px}

  .site-footer{position:absolute;left:0;top:989px;width:1200px;height:49px;font-size:12px;font-weight:300;color:var(--footer-ink)}
  .copyright{position:absolute;left:157px;top:15px}
  .payments{position:absolute;left:510px;top:11px;display:flex;gap:4px}
  .payments span{width:36px;height:23px;border-radius:2px}
  .footer-nav{position:absolute;right:53px;top:15px;display:flex;gap:9px}
</style>
</head>
<body>
  <header class="site-header">
    <div class="brand-name">ROVELLA</div>
    <nav class="header-tools" aria-label="Tools">
      <svg viewBox="0 0 28 28" aria-label="Menu"><path d="M3 6h22M3 14h22M3 22h22"/></svg>
      <svg viewBox="0 0 28 28" aria-label="Call"><path d="M6 3l5 1 2 6-3 2a15 15 0 0 0 6 6l2-3 6 2 1 5-3 3C12 25 3 16 3 6z" fill="#fff" stroke="none"/></svg>
      <svg viewBox="0 0 28 28" aria-label="Search"><circle cx="12" cy="12" r="9"/><path d="M19 19l7 7"/></svg>
    </nav>
  </header>

  <section class="intro">
    <h1>Private &amp; <strong>Busines</strong></h1>
    <h2>Personalised transport service</h2>
    <p>Lorem ipsum dolor sit amet, consectetur adipiscing elit, sed do eiusmod tempor incididunt ut labore et dolore magna aliqua. Ut enim ad minim veniam, quis nostrud exercitation ullamco laboris nisi ut aliquip ex ea commodo consequat. Duis aute irure dolor in reprehenderit in voluptate velit esse cillum dolore eu fugiat nulla pariatur.</p>
  </section>

  <aside class="quote">
    <h3>GET<span class="hl">INSTANT</span><b>QUOTE</b></h3>
    <div class="field">Origin (Public Location or Exact Address)</div>
    <div class="field">Destination (Public Location or Exact Add</div>
    <div class="option"><span class="option-icon"><svg width="9" height="9" viewBox="0 0 9 9"><path d="M4.5 0v9M0 4.5h9" stroke="#2b2b2b" stroke-width="1.6"/></svg></span>Add Stops</div>
    <div class="option"><span class="option-icon"><svg width="9" height="7" viewBox="0 0 9 7"><path d="M0 0h9L4.5 7z" fill="#2b2b2b"/></svg></span>Show Other Vehicles</div>
    <div class="btn">ESTIMATE<b>FARE</b></div>
    <small>*See <span>Price Guide</span> for extras</small>
  </aside>

  <section class="feature">
    <div class="feature-tiles">
      <div class="tile tile-luxury">
        <div class="tile-photo" role="img" aria-label="Close-up of a luxury car interior with gear stick and console"></div>
        <div class="tile-label">LUXURY</div>
      </div>
      <div class="tile tile-style">
        <div class="tile-photo" role="img" aria-label="Side view of a dark stretch limousine"></div>
        <div class="tile-label">STYLE</div>
      </div>
    </div>
    <p>Lorem ipsum dolor sit amet, consectetur adipiscing elit, sed do eiusmod tempor incididunt ut labore et dolore magna aliqua. Ut enim ad minim veniam, quis nostrud exercitation ullamco</p>
    <div class="btn">BOOK<b>NOW</b></div>
  </section>

  <section class="benefits">
    <div class="benefit">
      <svg viewBox="0 0 30 30" aria-hidden="true"><path d="M3 20c0-3 1-4 4-5l4-4h9l4 4c2 0 3 1 3 3v2zM12 12l-2 3h5v-3zM17 12v3h5l-3-3z"/><circle cx="9" cy="21" r="2.5"/><circle cx="22" cy="21" r="2.5"/></svg>
      <div>Consectetur adipiscing elit, sed do eiusmod tempor incididunt ut labore et dolore magna aliqua.</div>
    </div>
    <div class="benefit">
      <svg viewBox="0 0 30 30" aria-hidden="true"><path d="M14 2h2l1 9 10 5v3l-10-3-1 7 3 3v2l-4-1-4 1v-2l3-3-1-7-10 3v-3l10-5z"/></svg>
      <div>Consectetur adipiscing elit, sed do eiusmod tempor incididunt ut labore et dolore magna aliqua.</div>
    </div>
    <div class="benefit">
      <svg viewBox="0 0 30 30" aria-hidden="true" style="fill:none;stroke:#fff;stroke-width:2.5"><circle cx="15" cy="15" r="12"/><path d="M15 8v8h6"/></svg>
      <div>Consectetur adipiscing elit, sed do eiusmod tempor incididunt ut labore et dolore magna aliqua.</div>
    </div>
    <div class="benefit">
      <svg viewBox="0 0 30 30" aria-hidden="true"><path d="M3 8a2 2 0 0 1 2-2h20a2 2 0 0 1 2 2v3H3zM3 14h24v8a2 2 0 0 1-2 2H5a2 2 0 0 1-2-2zM6 18v2h6v-2z"/></svg>
      <div>Consectetur adipiscing elit, sed do eiusmod tempor incididunt ut labore et dolore magna aliqua.</div>
    </div>
  </section>

  <footer class="site-footer">
    <div class="copyright">© Copyright 2017 |&nbsp; Rovella.com</div>
    <div class="payments" aria-label="Accepted payment methods">
      <span style="background:#e9e9e9"></span>
      <span style="background:#1a3a6e"></span>
      <span style="background:#e4e4e4"></span>
      <span style="background:#2a7fc4"></span>
      <span style="background:#ececec"></span>
    </div>
    <nav class="footer-nav">
      <span>Home</span><span>Sitemap</span><span>Privacy Policy</span><span>Terms &amp; Conditions</span>
    </nav>
  </footer>
</body>
</html>
```